Flyer for Car Detailing Shop

I am opening a detailing shop. I am looking for a nice, easy to read single sided flyer I can hand out at car shows, hang in store windows and to my clients and customers to promote my business. I want it a little professional yet attention grabbing. I want someone to look at it and go "holy shit, thats a nice flyer" haha

Here are some things that must be included:
- Company Name: Brightfern Motorworks Detailing & Coatings
- Tag Line: The Science of Detailing
- Address: 4150 Harlow Rd, Larkfield, OH 44890
- www.brightfernmotor.example
- Find Us on social Media! ::insert facebook and instagram logo
Colors: Black, Lime Green and Purple for accents, etc

HAND WASH
- Express Wash start at $25
- Deluxe Wash Start at $50

EXTERIOR DETAILING
-Basic Packages Start at $160
- Deluxe Packages Start at $350

INTERIOR DETAILING
- Basic Packages Start at $60
- Deluxe Packages Start at $200

New Car Prep and Ceramic Coatings
*Consultation required prior to beginning work*
- Paint: Starting at $500
- Interior: Starting at $100
- Wheels Off: Starting at $200
- Trim: Starting at $100
- Windows: $50 windshield/ $25 per pane

Additional Services
- Scratch removal
- Ozone Treatment
- Headlight Restoration
- Chip Repair

```html
<!DOCTYPE html>
<html lang="en">
<head>
<meta charset="utf-8">
<title>Brightfern Motorworks Flyer</title>
<link href="https://fonts.googleapis.com/css2?family=Bebas+Neue&family=Source+Sans+3:wght@400;600;700&display=swap" rel="stylesheet">
<style>
:root{
  --lime:#8cc63f;
  --ink:#161616;
  --panel:#222;
  --panel-deep:#0e0e0e;
  --paper:#ffffff;
  --stage:#e9e9e7;
  --rule:#555;
}
*{box-sizing:border-box;margin:0;padding:0}
html,body{width:1200px;height:772px;overflow:hidden;background:var(--stage)}
body{font-family:"Source Sans 3",Arial,sans-serif;color:var(--ink)}
.flyer{position:absolute;left:315px;top:17px;width:612px;height:793px;background:var(--paper);transform:scale(.93);transform-origin:0 0;overflow:hidden;box-shadow:0 6px 18px rgba(0,0,0,.25)}
.abs{position:absolute}
.hero-photo{left:0;top:0;width:612px;height:410px;background:linear-gradient(180deg,#eef1ee 0%,#c9cfc6 40%,#8e958a 70%,#b6b8b2 100%)}
.hero-fade{left:0;top:0;width:612px;height:410px;background:linear-gradient(90deg,rgba(255,255,255,.85) 0%,rgba(255,255,255,0) 30%)}
.brand{left:22px;top:92px;width:150px;display:flex;align-items:center;gap:8px}
.brand-dot{width:18px;height:18px;border-radius:50%;background:var(--ink);flex:none}
.brand-name{font-family:"Bebas Neue",sans-serif;font-size:26px;line-height:.95;color:var(--ink);letter-spacing:.5px}
.thumb{width:100px;height:100px;border-radius:50%;border:4px solid var(--lime);box-shadow:0 0 0 2px #fff}
.thumb-a{left:10px;top:300px;background:radial-gradient(circle at 45% 40%,#c7c9cc,#5b5f63)}
.thumb-b{left:103px;top:322px;background:radial-gradient(circle at 60% 45%,#f2f3f5,#9aa1aa)}
.wave{left:0;top:330px}
.tagline{left:17px;top:449px;font-family:"Bebas Neue",sans-serif;font-size:35px;letter-spacing:.2px;color:var(--ink);white-space:nowrap}
.service{left:16px;width:292px;display:flex;gap:8px}
.service-icon{width:50px;height:50px;background:#1e1e1e;border-radius:2px;flex:none;display:flex;align-items:center;justify-content:center}
.service-body{flex:1;padding-top:2px}
.service-title{font-size:12.5px;font-weight:700;text-transform:uppercase;letter-spacing:.2px}
.price-row{display:flex;align-items:baseline;font-size:12px;line-height:15px;padding-left:2px}
.price-row::before{content:"•";margin-right:5px}
.leader{flex:1;border-bottom:1px dotted #555;margin:0 2px 3px}
.price{color:var(--lime);font-weight:700}
.panel{left:337px;top:322px}
.panel-content{left:350px;top:394px;width:232px;color:#fff}
.panel-title{font-family:"Bebas Neue",sans-serif;font-size:19px;color:var(--lime);letter-spacing:.2px;white-space:nowrap}
.panel-note{font-size:7.5px;color:#ddd;margin-top:-1px;margin-bottom:6px}
.prep-row{font-size:12px;padding:6px 0 5px 2px;border-bottom:1px dotted var(--rule);white-space:nowrap}
.prep-row:last-child{border-bottom:none}
.prep-row::before{content:"•";color:var(--lime);margin-right:5px}
.prep-row b{font-weight:700}
.extras{left:352px;top:577px;width:226px;height:125px;background:var(--lime);padding:9px 12px}
.extras-title{font-family:"Bebas Neue",sans-serif;font-size:20px;color:var(--ink);margin-bottom:3px}
.extra-row{display:flex;align-items:center;gap:7px;font-size:12px;font-weight:600;line-height:22px;color:var(--ink)}
.extra-icon{width:17px;height:17px;border:1.5px solid var(--ink);border-radius:2px;flex:none}
.footer-left{left:0;top:717px}
.footer-info{left:17px;top:728px;color:#fff;font-size:12.5px;line-height:17px}
.footer-name{color:var(--lime)}
.footer-line{display:flex;align-items:center;gap:6px}
.footer-url b{font-weight:700}
.social-label{left:337px;top:758px;font-family:"Bebas Neue",sans-serif;font-size:21px;color:var(--ink)}
.social-dot{top:752px;width:32px;height:32px;border-radius:50%;background:var(--ink)}
</style>
</head>
<body>
<div class="flyer">
  <div class="abs hero-photo" role="img" aria-label="Photo of a lowered black sedan with gold wheels parked on a suburban driveway"></div>
  <div class="abs hero-fade"></div>

  <div class="abs brand">
    <span class="brand-dot"></span>
    <span class="brand-name">Brightfern Motorworks</span>
  </div>

  <svg class="abs wave" width="612" height="130" viewBox="0 0 612 130">
    <path d="M0 40 C70 55 140 70 200 80 L337 42 L612 20 L612 130 L0 130 Z" fill="#fff"/>
    <path d="M190 76 L200 80 L337 42 L337 50 L202 88 L190 84 Z" fill="var(--ink)"/>
    <path d="M590 106 L612 98 L612 104 L590 112 Z" fill="var(--ink)"/>
  </svg>

  <div class="abs thumb thumb-a" role="img" aria-label="Close-up photo of detailing products on an engine bay"></div>
  <div class="abs thumb thumb-b" role="img" aria-label="Close-up photo of a white bumper being polished"></div>

  <h1 class="abs tagline">The Science of Detailing</h1>

  <div class="abs service" style="top:497px">
    <div class="service-icon">
      <svg width="36" height="26" viewBox="0 0 36 26"><path d="M4 14 L9 6 H27 L32 14 V21 H4 Z" fill="var(--lime)"/><circle cx="10" cy="21" r="3.5" fill="var(--lime)"/><circle cx="26" cy="21" r="3.5" fill="var(--lime)"/><rect x="11" y="8" width="14" height="5" fill="#1e1e1e"/></svg>
    </div>
    <div class="service-body">
      <div class="service-title">Hand Wash</div>
      <div class="price-row">Express Wash start at<span class="leader"></span><span class="price">$25</span></div>
      <div class="price-row">Deluxe Wash Start at<span class="leader"></span><span class="price">$50</span></div>
    </div>
  </div>

  <div class="abs service" style="top:564px">
    <div class="service-icon">
      <svg width="34" height="36" viewBox="0 0 34 36"><rect x="4" y="2" width="5" height="22" fill="var(--lime)"/><rect x="2" y="22" width="9" height="10" fill="var(--lime)"/><rect x="16" y="6" width="14" height="28" rx="3" fill="none" stroke="var(--lime)" stroke-width="2.5"/><path d="M19 11 H27 M19 16 H27 M19 21 H27 M19 26 H27" stroke="var(--lime)" stroke-width="2"/></svg>
    </div>
    <div class="service-body">
      <div class="service-title">Exterior Detailing</div>
      <div class="price-row">Basic Packages Start at<span class="leader"></span><span class="price">$160</span></div>
      <div class="price-row">Deluxe Packages Start at<span class="leader"></span><span class="price">$350</span></div>
    </div>
  </div>

  <div class="abs service" style="top:632px">
    <div class="service-icon">
      <svg width="30" height="36" viewBox="0 0 30 36"><rect x="9" y="2" width="12" height="18" rx="4" fill="var(--lime)"/><rect x="5" y="20" width="20" height="9" rx="3" fill="var(--lime)"/><rect x="2" y="16" width="4" height="14" rx="2" fill="var(--lime)"/><rect x="24" y="16" width="4" height="14" rx="2" fill="var(--lime)"/><rect x="8" y="29" width="14" height="5" fill="var(--lime)"/></svg>
    </div>
    <div class="service-body">
      <div class="service-title">Interior Detailing</div>
      <div class="price-row">Basic Packages Start at<span class="leader"></span><span class="price">$60</span></div>
      <div class="price-row">Deluxe Packages Start at<span class="leader"></span><span class="price">$200</span></div>
    </div>
  </div>

  <svg class="abs panel" width="260" height="386" viewBox="0 0 260 386">
    <defs><linearGradient id="panelShade" x1="0" y1="0" x2="0" y2="1"><stop offset="0" stop-color="var(--panel)"/><stop offset="1" stop-color="var(--panel-deep)"/></linearGradient></defs>
    <path d="M0 34 L256 0 L256 376 L244 386 L0 386 Z" fill="url(#panelShade)"/>
  </svg>

  <div class="abs panel-content">
    <div class="panel-title">New Car Prep and Ceramic Coatings</div>
    <div class="panel-note">*Consultation required prior to beginning work*</div>
    <div class="prep-row">PAINT: Starting at <b>$500</b></div>
    <div class="prep-row">INTERIOR: Starting at <b>$100</b></div>
    <div class="prep-row">WHEELS OFF: Starting at <b>$200</b></div>
    <div class="prep-row">TRIM: STARTING: at <b>$100</b></div>
    <div class="prep-row">WINDOWS: <b>$50</b> windshield/ <b>$25</b> per pane</div>
  </div>

  <div class="abs extras">
    <div class="extras-title">Additional Services</div>
    <div class="extra-row"><span class="extra-icon"></span>Scratch removal</div>
    <div class="extra-row"><span class="extra-icon"></span>Ozone Treatment</div>
    <div class="extra-row"><span class="extra-icon"></span>Headlight Restoration</div>
    <div class="extra-row"><span class="extra-icon"></span>Chip Repair</div>
  </div>

  <svg class="abs footer-left" width="612" height="76" viewBox="0 0 612 76">
    <path d="M0 0 H306 L316 26 H612 V76 H0 Z" fill="var(--lime)"/>
    <path d="M0 0 H306 L285 76 H0 Z" fill="#1b1b1b"/>
  </svg>

  <div class="abs footer-info">
    <div class="footer-name">Brightfern Motorworks Detailing &amp; Coatings</div>
    <div class="footer-line footer-url">
      <svg width="9" height="9" viewBox="0 0 10 10"><circle cx="5" cy="5" r="4" fill="none" stroke="var(--lime)" stroke-width="1.5"/><path d="M1 5 H9 M5 1 V9" stroke="var(--lime)" stroke-width="1"/></svg>
      <span>www.<b>brightfernmotor</b>.example</span>
    </div>
    <div class="footer-line">
      <svg width="9" height="12" viewBox="0 0 10 13"><path d="M5 0 C2 0 0 2 0 5 C0 8 5 13 5 13 C5 13 10 8 10 5 C10 2 8 0 5 0 Z" fill="var(--lime)"/><circle cx="5" cy="5" r="2" fill="#1b1b1b"/></svg>
      <span>4150 Harlow Rd, Larkfield, OH 44890</span>
    </div>
  </div>

  <div class="abs social-label">Find Us on Social Media!</div>
  <div class="abs social-dot" style="left:511px"></div>
  <div class="abs social-dot" style="left:552px"></div>
</div>
</body>
</html>
```